Realty Group Needs Classy, Contemporary Letterhead Design

We need a letterhead design for a new realty company located in NY, USA. We buy investment properties to rehabilitate and or keep in our rental portfolio.

```html
<!DOCTYPE html>
<html lang="en">
<head>
<meta charset="utf-8">
<title>Meridian Realty Group — Letterhead</title>
<link rel="stylesheet" href="https://fonts.googleapis.com/css2?family=Montserrat:wght@300;400;700&family=Source+Sans+3:wght@300;400;600;700&display=swap">
<style>
  :root {
    --canvas: #ebebed;
    --paper: #ffffff;
    --brand-purple: #4f2d84;
    --band-grey: #808080;
    --ink: #4a4a4a;
    --ink-soft: #6a6a6a;
  }
  * { box-sizing: border-box; margin: 0; padding: 0; }
  html, body {
    width: 1200px; height: 1200px; overflow: hidden;
    background: var(--canvas);
  }
  .letterhead {
    position: absolute; left: 196px; top: 35px;
    width: 807px; height: 1130px;
    background: var(--paper);
    font-family: "Source Sans 3", "Myriad Pro", sans-serif;
    color: var(--ink);
    box-shadow: 0 2px 6px rgba(0,0,0,0.08);
  }
  .side-band { position: absolute; left: 0; width: 40px; }
  .side-band--grey { top: 0; height: 565px; background: var(--band-grey); }
  .side-band--purple { top: 565px; height: 565px; background: var(--brand-purple); }

  .brand { position: absolute; left: 103px; top: 64px; display: flex; align-items: center; }
  .brand__mark { width: 36px; height: 36px; background: var(--brand-purple); margin-right: 14px; }
  .brand__name {
    font-family: "Source Sans 3", sans-serif; font-weight: 400;
    font-size: 27px; line-height: 1; color: var(--ink);
  }

  .contact { position: absolute; right: 67px; top: 46px; }
  .contact__row { display: flex; align-items: center; justify-content: flex-end; height: 36px; }
  .contact__text { font-family: "Montserrat", sans-serif; font-weight: 300; font-size: 11px; line-height: 13px; letter-spacing: 0.3px; text-align: right; color: var(--ink-soft); margin-right: 15px; }
  .contact__icon { width: 23px; height: 23px; display: flex; align-items: center; justify-content: center; }
  .contact__icon--grey { background: var(--band-grey); }
  .contact__icon--purple { background: var(--brand-purple); }

  .recipient { position: absolute; left: 104px; top: 265px; font-size: 14px; font-style: normal; }
  .recipient__name { display: block; line-height: 20px; font-size: 14.5px; }
  .recipient__title { display: block; font-size: 11.5px; line-height: 18px; margin-bottom: 4px; }
  .recipient__line { display: block; line-height: 23px; }
  .recipient__key { font-weight: 700; display: inline-block; width: 28px; }

  .letter-date { position: absolute; right: 78px; top: 352px; font-size: 14.5px; }

  .letter-body { position: absolute; left: 103px; top: 437px; font-size: 15.6px; letter-spacing: -0.25px; }
  .letter-body p { margin-bottom: 30px; }
  .letter-body span { display: block; line-height: 30px; white-space: nowrap; }

  .signature { position: absolute; left: 104px; top: 997px; }
  .signature__name { display: block; font-family: "Montserrat", sans-serif; font-weight: 700; font-size: 13.5px; line-height: 16px; color: var(--ink-soft); }
  .signature__role { display: block; font-family: "Montserrat", sans-serif; font-weight: 400; font-size: 12.5px; line-height: 16px; }
</style>
</head>
<body>
<main class="letterhead">
  <div class="side-band side-band--grey"></div>
  <div class="side-band side-band--purple"></div>

  <header class="brand">
    <div class="brand__mark"></div>
    <span class="brand__name">Meridian Realty Group</span>
  </header>

  <section class="contact">
    <div class="contact__row">
      <div class="contact__text">+212 55501 4820<br>+212 55501 4821</div>
      <div class="contact__icon contact__icon--grey">
        <svg width="12" height="12" viewBox="0 0 12 12"><path d="M1 4 Q6 0 11 4 L10 5.5 L8 4.6 L8 3.6 Q6 3 4 3.6 L4 4.6 L2 5.5 Z M3 6 H9 L10 10 H2 Z" fill="#fff"/></svg>
      </div>
    </div>
    <div class="contact__row">
      <div class="contact__text">meridianrealty.com<br>office@meridianrg.com</div>
      <div class="contact__icon contact__icon--purple">
        <svg width="13" height="13" viewBox="0 0 13 13" fill="none" stroke="#fff" stroke-width="1"><circle cx="6.5" cy="6.5" r="5.5"/><ellipse cx="6.5" cy="6.5" rx="2.4" ry="5.5"/><path d="M1 6.5 H12"/></svg>
      </div>
    </div>
    <div class="contact__row">
      <div class="contact__text">28 Linden Street<br>NY, USA</div>
      <div class="contact__icon contact__icon--grey">
        <svg width="10" height="13" viewBox="0 0 10 13"><path d="M5 0 A5 5 0 0 1 10 5 C10 8 5 13 5 13 C5 13 0 8 0 5 A5 5 0 0 1 5 0 Z" fill="#fff"/><circle cx="5" cy="5" r="1.8" fill="#808080"/></svg>
      </div>
    </div>
  </section>

  <address class="recipient">
    <span class="recipient__name">Alan Porter</span>
    <span class="recipient__title">Chief Director</span>
    <span class="recipient__line"><span class="recipient__key">A :</span>12-4, Harbor Lane Brooklyn - 1120</span>
    <span class="recipient__line"><span class="recipient__key">W :</span>hello@meridianrg.com, www.meridianrg.com</span>
    <span class="recipient__line"><span class="recipient__key">P :</span>+212 - 55501 - 4820</span>
  </address>

  <div class="letter-date">Date, 10 September, 2019</div>

  <article class="letter-body">
    <p>
      <span>This is a sample letter that has been placed to demonstrate typing remat (Your Company). letterhead</span>
      <span>design. When positioned properly, it will serve to work in harmony with all other elements letterhead.</span>
      <span>This letterhead design is meant to project an image</span>
    </p>
    <p>
      <span>This letterhead design is meant project an image of professionalism reliability. By using simple aligen</span>
      <span>we have created a very spacious feeling. The simplicity suggest rengththe spaciousnes contributes h</span>
      <span>aesthetics the layout. These basic qualities along with the (Your Company)</span>
    </p>
    <p>
      <span>look and helps reinforce the (Your Company) brand. letterhead design is meant to project an image p</span>
      <span>design. When positioned properly, it will serve to work in harmony all the other elements letterhead.</span>
      <span>sionalism and reliability.</span>
    </p>
    <p>
      <span>This letterhead design is based on the (Form of your logo) form (Your Company) logo. Each stationery</span>
      <span>we have created a very spacious feeling. The simplicity suggests strength the spaciousnes contribute</span>
      <span>part of the (Form of your logo).</span>
    </p>
  </article>

  <footer class="signature">
    <span class="signature__name">Mark Ellison</span>
    <span class="signature__role">Manager</span>
  </footer>
</main>
</body>
</html>
```